Overseas Property Tax Depreciation

We need a two sided flyer to promote our business and explain what we do. our website is www.tolvexhq.net.
The attached word file is what I would like on an A5 size flyer with one side showing the FAQ and the other the worked example. I would like these formatted much better than the are and in general style of the website. I will attach files for logos as well.

Business

```html
<!DOCTYPE html>
<html lang="en">
<head>
<meta charset="utf-8">
<title>Tolvex Depreciation – Two-Sided Flyer</title>
<link href="https://fonts.googleapis.com/css2?family=Questrial&family=Arimo:wght@400;700&display=swap" rel="stylesheet">
<style>
:root{
  --backdrop:#7d7d7d;
  --paper:#ffffff;
  --green:#19b512;
  --green-dark:#0c8a07;
  --green-bright:#35d22c;
  --orange:#f7a300;
  --orange-light:#ffc21a;
  --ink:#1d1d1d;
  --ink-soft:#3a3a3a;
  --cell:#e6e6e6;
  --cell-edge:#f7f7f7;
  --bar:#2b2b2b;
  --photo-sky:#b9c3cc;
  --photo-ground:#6f6a60;
}
*{box-sizing:border-box;margin:0;padding:0}
html,body{width:1200px;height:907px;overflow:hidden}
body{background:var(--backdrop);font-family:"Arimo",Arial,sans-serif;position:relative}
.page{position:absolute;top:97px;width:508px;height:711px;background:var(--paper);overflow:hidden;box-shadow:0 4px 14px rgba(0,0,0,.45)}
.page--faq{left:72px}
.page--example{left:637px;background:linear-gradient(180deg,var(--orange) 0%,var(--orange-light) 40%,#f2f2f2 62%,#eaeaea 100%)}

/* FAQ side */
.brand{position:absolute;left:40px;top:50px;width:165px;display:flex;align-items:center;gap:8px;z-index:3}
.brand__mark{flex:none;width:16px;height:16px;background:var(--orange);border-radius:50%}
.brand__name{font-family:"Questrial",sans-serif;font-size:21px;color:var(--green);line-height:1.05}
.intro{position:absolute;left:211px;top:21px;width:278px;height:150px;background:linear-gradient(90deg,#fff 0%,#fff1cf 40%,var(--orange) 100%);border-radius:10px;padding:0 10px;z-index:3}
.intro__title{background:linear-gradient(180deg,#fff,#eee);border-radius:8px;margin:7px -4px 6px;padding:3px 8px;font-family:"Questrial",sans-serif;font-weight:700;font-size:13px;color:var(--ink)}
.intro p{font-family:"Questrial",sans-serif;font-size:9.4px;line-height:1.2;color:var(--ink-soft);margin-bottom:7px;text-align:justify}
.photo{position:absolute;left:0;top:150px;width:508px;height:210px;background:linear-gradient(180deg,var(--photo-sky) 0%,#cfd4d6 45%,#8f8a80 70%,var(--photo-ground) 100%)}
.wave{position:absolute;left:0;width:508px}
.faq-body{position:absolute;left:0;top:340px;width:508px;height:356px;padding:0 18px;color:#fff}
.pill{display:inline-block;background:linear-gradient(180deg,#fff,#ddd);color:var(--ink);font-family:"Questrial",sans-serif;font-weight:700;font-size:11px;padding:2px 10px;border-radius:8px;margin:4px 0 4px -6px;min-width:210px}
.faq-body p,.faq-body li{font-size:8.9px;font-weight:700;line-height:1.24}
.faq-body ul{list-style:none;margin:3px 0}
.faq-body li{padding-left:9px;position:relative;margin-bottom:3px}
.faq-body li::before{content:"";position:absolute;left:0;top:3px;width:5px;height:5px;border-radius:50%;background:#fff}
.footer-band{position:absolute;left:0;bottom:0;width:508px;height:18px;background:linear-gradient(180deg,#ddd,#bdbdbd)}

/* Example side */
.q-pill{position:absolute;left:14px;background:var(--green-dark);color:#fff;font-family:"Questrial",sans-serif;font-weight:700;font-size:11px;padding:2px 10px;border-radius:8px}
.q-pill--wide{width:330px;font-size:11px;line-height:1.25}
.answer{position:absolute;left:14px;width:482px;font-size:9.4px;font-weight:700;color:var(--ink);line-height:1.22}
.answer .dot{display:inline-block;width:6px;height:6px;border-radius:50%;background:var(--green-dark);margin-right:4px}
.calc{position:absolute;left:28px;top:194px;width:445px;border-collapse:separate;border-spacing:2px 1px;font-size:7px;color:var(--ink)}
.calc td{background:linear-gradient(90deg,var(--cell-edge),var(--cell) 50%,var(--cell-edge));text-align:center;padding:0 2px;font-variant:small-caps;font-weight:700;line-height:1.05}
.calc td.ref{background:linear-gradient(180deg,#fff,#d6d6d6);font-size:10px;width:16px;border-radius:2px}
.calc td.num{font-size:9px;font-variant:normal;color:var(--ink-soft)}
.calc td.mine{background:var(--green);color:#fff;font-size:10px;font-variant:normal}
.calc td.head{font-size:11px;font-family:"Questrial",sans-serif}
.calc td.dark{background:var(--bar);color:#fff}
.calc td.dark.num{color:#fff}
.calc td.hl{color:var(--green-bright)}
.calc td.colhead{background:var(--bar);color:var(--orange-light);font-size:8px}
.calc td.none{background:transparent}
.badges{position:absolute;left:175px;top:658px;display:flex;gap:22px;align-items:center}
.badge{width:34px;height:34px;border-radius:50%;background:#fff;border:3px solid #6a3f9c}
.badge--green{border-color:#2a9a2a}
</style>
</head>
<body>

<section class="page page--faq">
  <div class="brand"><span class="brand__mark"></span><span class="brand__name">Tolvex Depreciation</span></div>

  <svg class="wave" style="top:118px" height="60" viewBox="0 0 508 60" aria-hidden="true">
    <path d="M0 20 Q250 70 508 5 L508 60 L0 60Z" fill="var(--orange)"/>
    <path d="M0 28 Q250 76 508 14 L508 60 L0 60Z" fill="var(--green)"/>
  </svg>
  <div class="photo" role="img" aria-label="Photo of a row of new houses behind a steel palisade fence"></div>

  <div class="intro">
    <h2 class="intro__title">What is Property Depreciation?</h2>
    <p>Just like you claim wear and tear on a car purchased for income producing purposes, you can also claim the depreciation of your investment property against your taxable income.</p>
    <p>There are 2 types available: depreciation on Plant and Equipment, and depreciation on the cost of construction. Plant and Equipment refers to items within the building like ovens, dishwashers, carpet and blinds etc. Both these costs can be offset against your assessable income.</p>
  </div>

  <svg class="wave" style="top:300px" height="70" viewBox="0 0 508 70" aria-hidden="true">
    <path d="M0 30 Q200 70 508 0 L508 70 L0 70Z" fill="var(--orange)"/>
    <path d="M0 40 Q210 78 508 10 L508 70 L0 70Z" fill="var(--green)"/>
  </svg>

  <div class="faq-body" style="background:linear-gradient(180deg,var(--green) 0%,var(--green-dark) 60%,var(--green) 100%)">
    <span class="pill">Why use us?</span>
    <p>There are several websites out there offering tax depreciation reports for Australian properties but there are very few who are appropriately qualified and approved by the Australian Tax Office (ATO) and offer the necessary Irish expertise. The Quantity Surveyor that prepares your report:</p>
    <ul>
      <li>Is Irish and qualified as a Quantity Surveyor in Ireland.</li>
      <li>Worked there during the "Celtic Tiger" period when construction costs were quite high.</li>
      <li>Has detailed knowledge of Irish construction methods and costs over the past 20 years. Irish buildings are generally much more expensive than Australia due to the climate, just think about how many Australian houses you have seen that have double glazing, central heating, insulation etc..</li>
      <li>Has a partnership arrangement with an Irish quantity surveying firm to carry out the property inspections required in most cases to maximize the deductions available.</li>
      <li>Is a chartered member of the CSRB.</li>
      <li>Maintains the Appropriate Professional Indemnity Insurance.</li>
    </ul>
    <span class="pill">My property is in Ireland does this make a difference?</span>
    <p>Division 43 of the Income Tax Assessment Act 1997 which deals with capital works depreciation states that it applies to buildings begun outside Australia after 21 August 1990 Sect 43.20 (1) (b). Your Australian tax return should cover your worldwide income. As long as the property is available to rent back in Ireland you are obliged by the ATO to report any income or loss on that property.</p>
    <span class="pill">Is my property too old?</span>
    <p>No, if your property was constructed after 1990 you can claim for both the construction cost element and the Plant and equipment. If it was built before then you can still claim the plant and equipment allowance. The easiest thing to do is to contact us with some details on your property and we can make an initial assessment of the possible annual savings.</p>
  </div>
  <div class="footer-band"></div>
</section>

<section class="page page--example">
  <div class="q-pill" style="top:22px">How much will the report cost?</div>
  <p class="answer" style="top:40px">Each scenario is different so www.tolvexhq.net/quote - contact us to obtain a quick quote for your situation. Generally the cost of the report is a fraction of the savings in any one year.</p>
  <p class="answer" style="top:82px"><span class="dot"></span>Our fee is fully tax deductible</p>
  <p class="answer" style="top:99px"><span class="dot"></span>You do NOT need to get this report done every year so the cost can be spread over several years</p>
  <div class="q-pill q-pill--wide" style="top:121px">I haven't included my property for the past couple of years on my tax return is this a problem?</div>
  <p class="answer" style="top:159px">No, in actual fact you could have been missing out on savings for a number of years, you can also use this report to claim a refund from the ATO for up to the past three years</p>

  <table class="calc">
    <colgroup><col style="width:16px"><col style="width:100px"><col style="width:60px"><col style="width:58px"><col style="width:58px"><col style="width:63px"><col style="width:65px"></colgroup>
    <tr style="height:26px"><td class="ref">Ref</td><td class="head">DESCRIPTION</td><td></td><td></td><td class="colhead" colspan="2">WITHOUT PROPERTY<br>TAX DEPRECIATION</td><td class="colhead" style="background:var(--green-dark);color:#fff">WITH PROPERTY DEPRECIATION REPORT</td></tr>
    <tr style="height:11px"><td class="none"></td><td></td><td></td><td></td><td class="colhead">EURO</td><td class="colhead">AUD</td><td class="colhead">AUD</td></tr>
    <tr style="height:19px"><td class="ref">A</td><td>Rental Income</td><td class="num">€1,200</td><td>Month</td><td class="num">€14,400</td><td class="num">$20,571</td><td class="mine">$20,571</td></tr>
    <tr style="height:22px"><td class="none"></td><td class="head">EXPENSES</td><td></td><td></td><td></td><td></td><td class="mine"></td></tr>
    <tr style="height:28px"><td class="ref">B</td><td>Annual Interest charged on outstanding Mortgage (4% apr)</td><td></td><td></td><td class="num">€12,040</td><td class="num">$17,200</td><td class="mine">$17,200</td></tr>
    <tr style="height:19px"><td class="ref">C</td><td>Property agent fees or commission</td><td></td><td></td><td class="num">€1,200</td><td class="num">$1,714</td><td class="mine">$1,714</td></tr>
    <tr style="height:13px"><td class="ref">D</td><td>Local Property Tax</td><td></td><td></td><td class="num">€250</td><td class="num">$357</td><td class="mine">$357</td></tr>
    <tr style="height:13px"><td class="ref">E</td><td>Repairs and Maintenance</td><td></td><td></td><td class="num">€2,000</td><td class="num">$2,857</td><td class="mine">$2,857</td></tr>
    <tr style="height:13px"><td class="ref">F</td><td>Home Insurance</td><td></td><td></td><td class="num">€450</td><td class="num">$643</td><td class="mine">$643</td></tr>
    <tr style="height:15px"><td class="ref">G</td><td>Cleaning Advertising et..</td><td></td><td></td><td class="num">€1,500</td><td class="num">$2,143</td><td class="mine">$2,143</td></tr>
    <tr style="height:17px"><td class="ref dark hl">H</td><td class="dark hl">Property Tax Depreciation</td><td class="dark"></td><td class="dark"></td><td class="dark num">€0</td><td class="dark num">$0</td><td class="mine">$15,000</td></tr>
    <tr style="height:17px"><td class="ref dark">I</td><td class="dark">Total Annual Expenses</td><td class="dark" colspan="2">Total (B to H)</td><td class="dark num">€17,440</td><td class="dark num">$24,914</td><td class="dark num hl">$39,914</td></tr>
    <tr style="height:17px"><td class="ref dark">J</td><td class="dark">Annual Rental Loss/Gain</td><td class="dark" colspan="2">(A less I)</td><td class="dark num">-€3,040</td><td class="dark num">-$4,343</td><td class="dark num hl">-$19,343</td></tr>
    <tr style="height:20px"><td class="ref">K</td><td>Your Annual Income from other sources</td><td></td><td></td><td></td><td class="num">$180,000</td><td class="mine">$180,000</td></tr>
    <tr style="height:22px"><td class="ref">L</td><td>Your Taxable Income after Rental Losses/Gains</td><td colspan="2">(K Plus J)</td><td></td><td class="num">$175,657</td><td class="mine">$160,657</td></tr>
    <tr style="height:20px"><td class="ref">M</td><td>Your Marginal Income Tax Rate (37% +2% medicare)</td><td></td><td class="num">39%</td><td></td><td></td><td class="mine"></td></tr>
    <tr style="height:14px"><td class="ref">N</td><td>Annual Tax Saving</td><td colspan="2">(J multiplied by M)</td><td></td><td class="num">$1,694</td><td class="mine">$7,544</td></tr>
    <tr style="height:22px"><td class="none"></td><td class="head">FOREIGN TAX CREDITS</td><td></td><td></td><td></td><td></td><td class="mine"></td></tr>
    <tr style="height:26px"><td class="ref">O</td><td>Non-resident Landlord withholding Tax (20% Ireland)</td><td colspan="2">(A multiplied by 20%)</td><td class="num">€2,880</td><td class="num">$4,114</td><td class="mine">$4,114</td></tr>
    <tr style="height:15px"><td class="ref dark">P</td><td class="dark">Nett Tax Savings</td><td class="dark" colspan="2">(N Plus O)</td><td class="dark"></td><td class="dark num">$5,808</td><td class="dark num">$11,658</td></tr>
    <tr style="height:48px"><td class="ref dark">Q</td><td class="dark">Additional money in your pocket (Australia) per year due to property tax depreciation</td><td class="dark"></td><td class="dark"></td><td class="dark"></td><td class="dark"></td><td class="dark num hl">$5,850</td></tr>
  </table>

  <svg class="wave" style="top:630px" height="81" viewBox="0 0 508 81" aria-hidden="true">
    <path d="M0 10 Q250 40 508 0 L508 81 L0 81Z" fill="var(--green)"/>
    <path d="M0 70 L508 70 L508 81 L0 81Z" fill="var(--orange)"/>
  </svg>
  <div class="badges">
    <span class="badge" role="img" aria-label="Surveying institute membership badge"></span>
    <span class="badge badge--green" role="img" aria-label="Registered tax practitioner badge"></span>
  </div>
</section>

</body>
</html>
```